Re-design existing website and add products for sale.

Our current website is very basic and cluttered. (emberfernwellness.com.au)We want a modern looking website that is easy to navigate. We also want to start selling essential oils and crystal products, so there needs to be a separate page for this. Also needs to be easily edited as we need to change the monthly oracle card with the description. Would like calming colours as we are all about natural healing. Alongside the services listed there should be a button to book now which asks for their name, email, phone number ect. and adds it to the cart.

• Logo is still being designed, please leave a space for the logo which will basically be a lotus flower within a mandala.

```html
<!DOCTYPE html>
<html lang="en">
<head>
<meta charset="utf-8">
<title>Ember Fern Wellness</title>
<link rel="stylesheet" href="https://fonts.googleapis.com/css2?family=PT+Serif:wght@700&family=Roboto+Condensed:wght@400&family=Nunito:wght@400;600&family=Roboto:wght@400;500&display=swap">
<style>
:root{
  --cream:#fbf7ec;
  --cream-deep:#faf5e6;
  --teal:#5ab4b7;
  --teal-soft:#78c3c5;
  --mauve:#8a5a7c;
  --ink:#222222;
  --muted:#555555;
  --white:#ffffff;
  --line:#333333;
}
*{box-sizing:border-box;margin:0;padding:0}
html,body{width:1200px;height:3435px;overflow:hidden}
body{background:var(--white);font-family:'Roboto',Arial,sans-serif;color:var(--ink);position:relative}
.abs{position:absolute}
.center-x{left:0;right:0;text-align:center}

/* header */
.site-header{position:absolute;left:0;top:0;width:1200px;height:135px;background:var(--cream)}
.brand{position:absolute;left:88px;top:46px;display:flex;align-items:center;gap:12px;font-family:'Nunito',sans-serif;font-weight:600;font-size:28px;color:var(--teal)}
.brand-dot{width:34px;height:34px;border-radius:50%;border:2px solid var(--teal)}
.main-nav a{position:absolute;top:53px;font-family:'Roboto',sans-serif;font-size:19px;color:var(--ink);text-decoration:none}
.main-nav a.active{color:var(--teal)}

/* hero */
.hero{position:absolute;left:0;top:135px;width:1200px;height:517px;overflow:hidden}
.hero-photo{position:absolute;inset:0;background:radial-gradient(ellipse at 60% 35%,#6a5bc4 0%,#3a2f86 35%,#1f2a5a 65%,#1b4a4a 100%)}
.hero-title{top:155px;font-family:'PT Serif',serif;font-weight:700;font-size:62px;color:var(--white)}
.hero-sub{top:243px;font-family:'Roboto Condensed',sans-serif;font-size:31px;color:var(--white)}
.hero-btn{position:absolute;left:518px;top:311px;width:164px;height:48px;border:3px solid var(--white);color:var(--white);font-family:'Roboto',sans-serif;font-weight:500;font-size:22px;display:flex;align-items:center;justify-content:center}
.hero-dots{position:absolute;left:1153px;top:215px;display:flex;flex-direction:column;gap:13px}
.hero-dots span{width:8px;height:8px;border-radius:50%;background:var(--white)}

/* headings */
.section-title{font-family:'Nunito',sans-serif;font-weight:400;font-size:44px;color:var(--ink)}

/* services */
.service-photo{position:absolute;top:840px;width:306px;height:197px}
.service-name{position:absolute;top:1062px;width:306px;text-align:center;font-family:'Roboto',sans-serif;font-size:24px;color:var(--ink)}
.service-desc{position:absolute;top:1104px;width:306px;text-align:center;font-size:15px;line-height:23px;color:var(--muted)}
.service-btn{position:absolute;top:1170px;width:165px;height:36px;border:2px solid var(--line);display:flex;align-items:center;justify-content:center;font-size:16px;color:var(--ink)}
.arrow{position:absolute}

/* about */
.about{position:absolute;left:0;top:1303px;width:1200px;height:517px;overflow:hidden}
.about-photo{position:absolute;inset:0;background:radial-gradient(ellipse at 50% 85%,#6b4a33 0%,#3a2418 40%,#1a100b 80%)}
.about-title{top:66px;font-family:'Nunito',sans-serif;font-size:44px;color:var(--white)}
.about-text{position:absolute;left:236px;top:128px;width:728px;text-align:center;font-family:'Nunito',sans-serif;font-size:16px;line-height:27px;color:var(--white)}

/* products */
.product-card{position:absolute;top:2006px;width:316px;height:396px;background:var(--white);box-shadow:0 2px 8px rgba(0,0,0,.25)}
.product-photo{position:absolute;left:12px;top:12px;width:292px;height:258px}
.product-name{position:absolute;left:0;right:0;top:292px;text-align:center;font-family:'Nunito',sans-serif;font-weight:600;font-size:24px;color:var(--ink)}
.product-btn{position:absolute;left:95px;top:341px;width:126px;height:34px;background:var(--teal);color:var(--white);font-size:16px;font-weight:500;display:flex;align-items:center;justify-content:center}

/* contact */
.contact{position:absolute;left:0;top:2514px;width:1200px;height:699px;background:var(--cream-deep)}
.contact-lead{top:132px;font-size:15px;line-height:23px;color:var(--muted)}
.contact-line{font-family:'Nunito',sans-serif;font-size:19px;color:var(--ink)}
.field{position:absolute;left:307px;width:586px;border:1.5px solid var(--line);background:var(--white);font-size:15px;color:var(--ink);padding:10px 22px}
.submit-btn{position:absolute;left:776px;top:577px;width:117px;height:37px;background:var(--mauve);color:var(--white);font-size:18px;display:flex;align-items:center;justify-content:center}

/* footer */
.site-footer{position:absolute;left:0;top:3213px;width:1200px;height:222px;background:var(--teal)}
.sub-title{position:absolute;left:87px;top:55px;font-family:'Nunito',sans-serif;font-size:22px;color:var(--white)}
.sub-input{position:absolute;left:87px;top:98px;width:309px;height:48px;border:1.5px solid var(--white);color:var(--white);font-size:15px;padding:12px 10px}
.sub-btn{position:absolute;left:403px;top:98px;width:126px;height:48px;background:var(--mauve);color:var(--white);font-size:19px;display:flex;align-items:center;justify-content:center}
.footer-info{position:absolute;left:735px;font-family:'Nunito',sans-serif;font-size:17px;color:var(--white)}
</style>
</head>
<body>

<header class="site-header">
  <div class="brand"><span class="brand-dot"></span>Ember Fern Wellness</div>
  <nav class="main-nav">
    <a class="active" style="left:508px">Home</a>
    <a style="left:627px">About</a>
    <a style="left:745px">Services</a>
    <a style="left:891px">Products</a>
    <a style="left:1041px">Contact</a>
  </nav>
</header>

<section class="hero">
  <div class="hero-photo" role="img" aria-label="Hand holding an amethyst crystal against a glowing purple and teal energy swirl with sparkles"></div>
  <h1 class="abs center-x hero-title">Ember Fern Wellness</h1>
  <p class="abs center-x hero-sub">Find Your True Self and Bring Balance to Your Life</p>
  <div class="hero-btn">Book Now</div>
  <div class="hero-dots"><span></span><span></span><span></span><span></span></div>
</section>

<section class="services">
  <h2 class="abs center-x section-title" style="top:732px">Our Services</h2>
  <svg class="arrow" style="left:46px;top:921px" width="20" height="36" viewBox="0 0 20 36"><path d="M18 2 L3 18 L18 34" fill="none" stroke="#555" stroke-width="2"/></svg>
  <svg class="arrow" style="left:1134px;top:921px" width="20" height="36" viewBox="0 0 20 36"><path d="M2 2 L17 18 L2 34" fill="none" stroke="#555" stroke-width="2"/></svg>

  <div class="service-photo" style="left:92px;background:radial-gradient(circle at 50% 35%,#f3d27a 0%,#b0602e 35%,#4a1d1a 80%)" role="img" aria-label="Cupped hands beneath a glowing golden spiral of energy"></div>
  <h3 class="service-name" style="left:92px">Reiki/Seichim Healings</h3>
  <p class="service-desc" style="left:92px">Reiki is a non-intrusive, wonderful<br>hands-on healing technique,</p>
  <div class="service-btn" style="left:162px">Book Now</div>

  <div class="service-photo" style="left:447px;background:linear-gradient(180deg,#c84fd0 0%,#7a7de0 50%,#3c8fc0 100%)" role="img" aria-label="Silhouette meditating in lotus pose with glowing chakra points"></div>
  <h3 class="service-name" style="left:447px">Reiki &amp; Seichim Workshops</h3>
  <p class="service-desc" style="left:447px">Have you had the chance to experi-<br>ence Reiki or Seichim and now wish</p>
  <div class="service-btn" style="left:518px">Book Now</div>

  <div class="service-photo" style="left:801px;background:radial-gradient(circle at 50% 55%,#ffffff 0%,#f7a6d8 20%,#8c3fc4 55%,#2e1a6a 100%)" role="img" aria-label="Two hands around a bright multicoloured light orb"></div>
  <h3 class="service-name" style="left:801px">Chakra Balancing</h3>
  <p class="service-desc" style="left:801px">Reiki is a non-intrusive, wonderful<br>hands-on healing technique,</p>
  <div class="service-btn" style="left:872px">Book Now</div>
</section>

<section class="about">
  <div class="about-photo" role="img" aria-label="Cupped hands holding raw quartz crystals surrounded by lit candles"></div>
  <h2 class="abs center-x about-title">About Us</h2>
  <p class="about-text">It is a long established fact that a reader will be distracted by the readable content of a page when looking at its layout. The point of using Lorem Ipsum is that it has a more-or-less normal distribution of letters, as opposed to using 'Content here, content here', making it look like readable English. Many desktop publishing packages.</p>
</section>

<section class="products">
  <h2 class="abs center-x section-title" style="top:1907px">Our Products</h2>
  <svg class="arrow" style="left:43px;top:2147px" width="20" height="36" viewBox="0 0 20 36"><path d="M18 2 L3 18 L18 34" fill="none" stroke="#555" stroke-width="2"/></svg>
  <svg class="arrow" style="left:1130px;top:2147px" width="20" height="36" viewBox="0 0 20 36"><path d="M2 2 L17 18 L2 34" fill="none" stroke="#555" stroke-width="2"/></svg>

  <div class="product-card" style="left:98px">
    <div class="product-photo" style="background:radial-gradient(circle at 50% 50%,#c2483f 0%,#e9a39a 45%,#f4f4f4 80%)" role="img" aria-label="Red crystal chips with pink salt"></div>
    <div class="product-name">Product Name</div>
    <div class="product-btn">Shop Now</div>
  </div>
  <div class="product-card" style="left:442px">
    <div class="product-photo" style="background:radial-gradient(circle at 50% 60%,#d98a1e 0%,#efc27c 35%,#f4f4f4 75%)" role="img" aria-label="Glass bottle of amber essential oil"></div>
    <div class="product-name">Product Name</div>
    <div class="product-btn">Shop Now</div>
  </div>
  <div class="product-card" style="left:784px">
    <div class="product-photo" style="background:radial-gradient(circle at 50% 50%,#9a7fc2 0%,#b9d6a4 35%,#f0c48a 55%,#f4f4f4 85%)" role="img" aria-label="Coloured leaves arranged in a circle with tumbled crystals"></div>
    <div class="product-name">Product Name</div>
    <div class="product-btn">Shop Now</div>
  </div>
</section>

<section class="contact">
  <h2 class="abs center-x section-title" style="top:70px">Contact</h2>
  <p class="abs center-x contact-lead">Please feel free to contact me by phone or email.<br>Or alternatively fill in the form below, and I will get back to you as soon as I can.</p>
  <p class="abs center-x contact-line" style="top:207px">PHONE NUMBER: 123-456-7890</p>
  <p class="abs center-x contact-line" style="top:242px">EMAIL: info@emberfernwellness.com.au</p>
  <div class="field" style="top:305px;height:45px">Name</div>
  <div class="field" style="top:358px;height:46px">Email</div>
  <div class="field" style="top:410px;height:46px">Subject</div>
  <div class="field" style="top:463px;height:104px">Message</div>
  <div class="submit-btn">Submit</div>
</section>

<footer class="site-footer">
  <div class="sub-title">Subscribe for Updates</div>
  <div class="sub-input">Email Address</div>
  <div class="sub-btn">Subscribe</div>
  <p class="footer-info" style="top:64px">27 Willow Bend Rd., Byron Bay, NSW 2481</p>
  <p class="footer-info" style="top:99px">Tel: 123-456-7890, info@emberfernwellness.com.au</p>
  <p class="footer-info" style="top:138px">© 2019 Company Name &nbsp;All right reserved</p>
</footer>

</body>
</html>
```